Updated Business Card Re-design (Logo Provided)

I am needing to update our business cards for our practice, Bright Harbor Care. We are a personal injury and wellness practice. The final design should be elegant and classy, but a type of card people would want to keep. Any samples should only have Dr. Tarek Minouvel on the template.
Updates

Went on vacation/holiday

Need extra days to review

Target Market(s)

Personal Injury clients, wellness clients

Industry/Entity Type

Personal Injury, medical, wellness

Contact Information for Business Card

dr and practice name, offerings

Requirements
Must have
• Single sided, this will be printed on a transparent business card, no exceptions.

```html
<!DOCTYPE html>
<html lang="en">
<head>
<meta charset="utf-8">
<title>Bright Harbor Care – Business Cards</title>
<link href="https://fonts.googleapis.com/css2?family=Roboto:wght@400;500;700&display=swap" rel="stylesheet">
<style>
  :root {
    --page: #ffffff;
    --card: #ffffff;
    --brand-blue: #1a75bb;
    --brand-orange: #f0901e;
    --ink: #333333;
    --ink-strong: #111111;
    --shadow: rgba(0,0,0,0.55);
  }
  * { margin: 0; padding: 0; box-sizing: border-box; }
  html, body {
    width: 1200px; height: 1200px; overflow: hidden;
    background: var(--page);
    font-family: "Roboto", Arial, sans-serif;
  }
  .canvas { position: relative; width: 1200px; height: 1200px; }
  .card {
    position: absolute; width: 652px; height: 372px;
    background: var(--card);
    box-shadow: 6px 6px 6px var(--shadow);
    overflow: hidden;
  }
  .card--detailed { left: 284px; top: 174px; }
  .card--feature { left: 278px; top: 614px; }

  .brand { position: absolute; left: 36px; top: 46px; display: flex; align-items: center; gap: 12px; }
  .brand__dot { width: 30px; height: 30px; border-radius: 50%; background: var(--brand-orange); }
  .brand__name { font-size: 34px; font-weight: 700; color: var(--brand-blue); letter-spacing: -0.5px; }
  .tagline {
    position: absolute; left: 36px; top: 112px;
    font-size: 21px; font-weight: 700; color: var(--brand-orange);
  }

  .provider { position: absolute; top: 170px; width: 320px; text-align: center; color: var(--ink); }
  .provider--right { left: 322px; }
  .provider__name { font-size: 25px; font-weight: 700; line-height: 1.1; }
  .provider__assoc { font-size: 14px; margin-top: 4px; letter-spacing: 0.3px; }

  .services { position: absolute; left: 44px; top: 244px; font-size: 21px; color: var(--ink); line-height: 27px; letter-spacing: 0.4px; }
  .services .sep { display: inline-block; width: 1.5px; height: 23px; background: var(--ink); vertical-align: -4px; margin: 0 6px; }

  .contact { position: absolute; left: 122px; top: 322px; display: flex; align-items: center; gap: 8px;
    font-size: 25px; font-weight: 700; color: var(--ink); }
  .contact svg { flex: none; }
  .contact__item + .contact__item { margin-left: 10px; }

  .feature { position: absolute; left: 0; width: 100%; text-align: center; }
  .feature__name { top: 166px; font-size: 52px; font-weight: 700; color: var(--ink-strong); }
  .feature__assoc { top: 226px; font-size: 29px; color: var(--ink); letter-spacing: 0.6px; left: 4px; }
</style>
</head>
<body>
<main class="canvas">

  <section class="card card--detailed" aria-label="Business card with full details">
    <div class="brand"><span class="brand__dot"></span><span class="brand__name">Bright Harbor Care</span></div>
    <p class="tagline">Riverbend Spine and Disc</p>

    <div class="provider provider--right">
      <p class="provider__name">Dr. Tarek Minouvel</p>
      <p class="provider__assoc">Lionel B Harwick, PT, ATC, MS</p>
    </div>

    <p class="services">
      Auto Accident Care<span class="sep"></span>Primary Care<span class="sep"></span>Medical Weight loss<br>
      Physical Therapy<span class="sep"></span>Chiropractic
    </p>

    <div class="contact">
      <svg width="26" height="26" viewBox="0 0 24 24" fill="none" stroke="#333" stroke-width="1.4" aria-hidden="true">
        <path d="M5 3h4l2 5-2.5 1.5a11 11 0 0 0 6 6L16 13l5 2v4a2 2 0 0 1-2 2A16 16 0 0 1 3 5a2 2 0 0 1 2-2z"/>
      </svg>
      <span class="contact__item">555 014 2286</span>
      <svg class="contact__item" width="16" height="26" viewBox="0 0 16 26" fill="none" stroke="#333" stroke-width="2.2" aria-hidden="true">
        <rect x="2" y="2" width="12" height="22" rx="1"/><line x1="2" y1="19" x2="14" y2="19"/>
      </svg>
      <span>555 019 4731</span>
    </div>
  </section>

  <section class="card card--feature" aria-label="Business card for Dr. Tarek Minouvel">
    <div class="brand"><span class="brand__dot"></span><span class="brand__name">Bright Harbor Care</span></div>
    <p class="tagline">Riverbend Spine and Disc</p>
    <p class="feature feature__name">Dr. Tarek Minouvel</p>
    <p class="feature feature__assoc">Lionel B Harwick, PT, ATC, MS</p>
  </section>

</main>
</body>
</html>
```